VELOTRAK End User Instruction Guide

I need to create a 5 to 7-page instruction guides for customers who purchased a phone system from our company. The document is a quick reference guide that will help end-users learn how to set up and use their new desk phone and software applications. I need the guide to be 3 x 5 or 6 x 8 in size and will fold like a book.

Target Market(s)

Business users / Brontel Desk Phone Users / VeLOTRAK Portal users

Industry/Entity Type

Telecommunications

Font styles to use
Serif

Colors
0758a5
ffffff

Requirements
Must have
• Need to have step-by-step instructions that include the information from the QuickStart guide I provided. I need to see an image of the phone with an arrow pointing to the key on the phone that should be pressed. For example, when checking voicemail the Messages key is pressed and I want to highlight this button or call it out somehow.

I need to have three pages for setup instructions, one page for shortcuts or features codes and our support contacts on the last page.
Nice to have
• I want to have a page for notes that the end-user can use during training. I would also like to have a blank space next to passwords and user ID's so they can be filled out with specific details that are provided during their training. For example, in the voicemail section, I include a default PIN. I would like to leave this blank and let the end-user fill it out during training.
Should not have
• Complex shapes and designs. I like straight lines and a simple easy to understand layout.

```html
<!DOCTYPE html>
<html lang="en">
<head>
<meta charset="UTF-8">
<title>VELOTRAK End User Quick Start Guide</title>
<link href="https://fonts.googleapis.com/css2?family=Roboto:wght@300;400;500;700&display=swap" rel="stylesheet">
<style>
  :root {
    --brand-blue: #0758a5;
    --brand-navy: #263c66;
    --white: #ffffff;
    --device-dark: #2c3137;
    --device-mid: #4a5058;
  }
  html, body {
    margin: 0;
    padding: 0;
    overflow: hidden;
    background: var(--white);
  }
  .cover {
    position: relative;
    width: 900px;
    height: 1200px;
    overflow: hidden;
    background: var(--white);
    font-family: "Roboto", Arial, sans-serif;
  }
  .cover-shapes {
    position: absolute;
    inset: 0;
  }
  .brand {
    position: absolute;
    left: 70px;
    top: 84px;
    display: flex;
    align-items: center;
    gap: 14px;
  }
  .brand-square {
    width: 46px;
    height: 46px;
    background: var(--brand-navy);
  }
  .brand-name {
    font-size: 46px;
    font-weight: 700;
    letter-spacing: 1px;
    color: var(--brand-navy);
    line-height: 1;
  }
  .tagline {
    position: absolute;
    left: 543px;
    top: 89px;
    margin: 0;
    font-size: 19px;
    font-weight: 500;
    color: var(--brand-blue);
    letter-spacing: 0.1px;
  }
  .title {
    position: absolute;
    left: 0;
    width: 874px;
    top: 382px;
    margin: 0;
    text-align: center;
    font-size: 74px;
    font-weight: 300;
    line-height: 88px;
    color: var(--brand-blue);
  }
  .subtitle {
    position: absolute;
    left: 101px;
    top: 707px;
    margin: 0;
    font-size: 19px;
    font-weight: 300;
    line-height: 25px;
    color: var(--white);
    text-transform: uppercase;
  }
  .device-image {
    position: absolute;
    left: 345px;
    top: 710px;
    width: 435px;
    height: 258px;
  }
</style>
</head>
<body>
  <main class="cover">
    <svg class="cover-shapes" width="900" height="1200" viewBox="0 0 900 1200" aria-hidden="true">
      <polygon class="header-band" points="440,140 900,140 900,170 422,170" fill="var(--brand-blue)"/>
      <polygon class="hero-wedge" points="0,562 900,860 0,860" fill="var(--brand-blue)"/>
    </svg>

    <div class="brand">
      <span class="brand-square"></span>
      <span class="brand-name">VELOTRAK</span>
    </div>
    <p class="tagline">AT VeLOTRAK, WE MAKE IT EASY</p>

    <h1 class="title">End User Quick<br>Start Guide</h1>

    <p class="subtitle">To set up and use<br>new desk phone and<br>software applications</p>

    <svg class="device-image" viewBox="0 0 435 258" role="img" aria-label="Photo of a Brontel desk phone with colour display, handset and keypad">
      <defs>
        <linearGradient id="deviceTone" x1="0" y1="0" x2="0" y2="1">
          <stop offset="0" stop-color="var(--device-dark)"/>
          <stop offset="1" stop-color="var(--device-mid)"/>
        </linearGradient>
      </defs>
      <rect x="0" y="0" width="435" height="258" rx="14" fill="url(#deviceTone)"/>
    </svg>
  </main>
</body>
</html>
```